Values-Driven Leadership Slides

Hello. I am creating a leadership framework. I need 5 PowerPoint slides to show how my values (and sub-values) align with actions. The attached file shows the content that should be on each slide. As you will see, the first slide should be a "summary" view of all, and the four other slides should be fully readable. Please use a font available on most computers. (I envision a constellation where I can "zoom in" on individual sections, but I'm open to various concepts.)

```html
<!DOCTYPE html>
<html lang="en">
<head>
<meta charset="utf-8">
<title>Value-Driven Leadership</title>
<link href="https://fonts.googleapis.com/css2?family=Arimo:wght@400;700&family=Carlito:wght@400;700&display=swap" rel="stylesheet">
<style>
:root{
  --canvas:#a8a8a8;
  --white:#ffffff;
  --ink:#2f2f2f;
  --cyan:#00aeef;
  --cyan-pill:#27c2f5;
  --green:#7cc242;
  --green-pill:#8fd24f;
  --gold:#f4b400;
  --gold-pill:#ffc20e;
  --navy:#1f3a6c;
  --navy-pill:#2c4c92;
  --brand-blue:#0a6fc2;
}
*{box-sizing:border-box;margin:0;padding:0}
html,body{width:1200px;height:1019px;overflow:hidden}
body{background:var(--canvas);position:relative;font-family:"Carlito","Calibri",sans-serif}
.slide{position:absolute;width:593px;height:333px;background:var(--white);overflow:hidden}
.s-summary{left:5px;top:5px}
.s-connection{left:602px;top:5px}
.s-growth{left:5px;top:342px}
.s-justice{left:602px;top:342px}
.s-joy{left:5px;top:681px}

/* summary */
.deco{position:absolute;left:0;top:0}
.summary-title{position:absolute;left:53px;top:9px;font:700 17px "Arimo",sans-serif;color:var(--white)}
.page-no{position:absolute;right:9px;bottom:6px;font:400 8px "Arimo",sans-serif;color:var(--white)}
.tile{position:absolute;left:38px;width:52px;height:51px;border-radius:8px;box-shadow:0 3px 6px rgba(0,0,0,.25);color:var(--white);font:700 7.5px "Carlito",sans-serif;text-align:center}
.tile .disc{display:block;width:28px;height:28px;border-radius:50%;background:var(--white);margin:7px auto 3px;position:relative}
.band{position:absolute;left:104px;width:467px;height:54px;border-radius:12px}
.band .col{position:absolute;top:0;height:100%;display:flex;align-items:center}
.band .col+.col{border-left:1px solid rgba(255,255,255,.25)}
.band ul{list-style:disc;padding-left:8px;color:var(--white);font-size:5.6px;line-height:8.6px}
.mini-pill{position:absolute;height:16px;width:78px;border-radius:8px;color:var(--white);font:700 8.5px "Carlito",sans-serif;display:flex;align-items:center;justify-content:center;box-shadow:0 2px 4px rgba(0,0,0,.2)}

.cyan{background:var(--cyan)} .cyan-pill{background:var(--cyan-pill)}
.green{background:var(--green)} .green-pill{background:var(--green-pill)}
.gold{background:var(--gold)} .gold-pill{background:var(--gold-pill)}
.navy{background:var(--navy)} .navy-pill{background:var(--navy-pill)}

/* detail slides */
.photo{position:absolute;left:0;top:0;width:313px;height:333px}
.photo-connection{background:linear-gradient(135deg,#3a4340 0%,#2b3a31 45%,#1d2523 100%)}
.photo-growth{background:linear-gradient(120deg,#4b4b4b 0%,#2e2e2e 55%,#3a3733 100%)}
.photo-justice{background:linear-gradient(135deg,#3d4146 0%,#2a2d31 55%,#1c1e21 100%)}
.photo-joy{background:linear-gradient(180deg,#2a3340 0%,#5a4a4a 38%,#6e5347 46%,#2b3540 60%,#1c2530 100%)}
.badge{position:absolute;width:52px;height:51px;border-radius:7px;color:var(--white);font:700 7.5px "Carlito",sans-serif;text-align:center;box-shadow:0 3px 6px rgba(0,0,0,.3)}
.badge .disc{display:block;width:28px;height:28px;border-radius:50%;background:var(--white);margin:6px auto 3px;position:relative}
.disc i{position:absolute;bottom:7px;width:3px;border-radius:1px}
.disc .ring{position:absolute;inset:7px;border-radius:50%;border:2px solid currentColor}
.headline{position:absolute;color:var(--white);font-family:"Arimo",sans-serif;line-height:35px}
.headline b{display:block;font-weight:700;font-size:25px}
.headline span{display:block;font-weight:400;font-size:26px}
.pill{position:absolute;height:23px;border-radius:12px;color:var(--white);font:700 11px "Arimo",sans-serif;display:flex;align-items:center;justify-content:center;letter-spacing:.2px;box-shadow:0 2px 5px rgba(0,0,0,.25)}
.item{position:absolute;font:400 10px "Carlito",sans-serif;color:var(--ink);white-space:nowrap;transform:translateY(-50%)}
.item::before{content:"";position:absolute;left:-21px;top:50%;width:12px;height:12px;margin-top:-6px;border-radius:50%;background:var(--tick);box-shadow:0 0 0 1.5px var(--white)}
.item::after{content:"";position:absolute;left:-17px;top:50%;width:3px;height:6px;margin-top:-4.5px;border:solid var(--white);border-width:0 1.6px 1.6px 0;transform:rotate(45deg)}
.s-connection{--tick:var(--cyan)}
.s-growth{--tick:var(--green)}
.s-justice{--tick:var(--gold)}
.s-joy{--tick:var(--navy-pill)}
</style>
</head>
<body>

<!-- Summary slide -->
<section class="slide s-summary">
  <svg class="deco" width="593" height="333" viewBox="0 0 593 333" aria-hidden="true">
    <path d="M0 0H502Q470 30 440 30H70Q30 30 0 58Z" fill="var(--brand-blue)"/>
    <path d="M306 333Q330 313 360 313H560Q580 313 593 298V333Z" fill="var(--brand-blue)"/>
  </svg>
  <h1 class="summary-title">Value-Driven Leadership</h1>

  <div class="tile cyan" style="top:56px"><span class="disc" style="color:var(--cyan)"><span class="ring"></span></span>Connection</div>
  <div class="tile green" style="top:121px"><span class="disc"><i style="left:8px;height:5px;background:var(--green)"></i><i style="left:12px;height:8px;background:var(--green)"></i><i style="left:16px;height:11px;background:var(--green)"></i></span>Growth</div>
  <div class="tile gold" style="top:187px"><span class="disc" style="color:var(--gold)"><span class="ring"></span></span>Justice</div>
  <div class="tile navy" style="top:252px"><span class="disc" style="color:var(--navy)"><span class="ring"></span></span>Joy</div>

  <div class="band cyan" style="top:53px">
    <div class="col" style="left:18px;width:102px"><ul><li>Be reliable.</li><li>Right wrongs.</li><li>Be honest.</li><li>Keep confidences</li></ul></div>
    <div class="col" style="left:122px;width:180px;padding-left:10px"><ul><li>Treat people as “human beings,” not “human doings.”</li><li>Believe that people are doing their best.</li></ul></div>
    <div class="col" style="left:302px;width:165px;padding-left:10px"><ul><li>Amplify voices of marginalized people.</li><li>Co-create safe spaces for diverse groups.</li></ul></div>
  </div>
  <div class="band green" style="top:118px">
    <div class="col" style="left:18px;width:104px"><ul><li>Listen to learn.</li><li>Maintain a growth mindset.</li><li>Stay curious.</li><li>Ask excellent questions.</li></ul></div>
    <div class="col" style="left:122px;width:180px;padding-left:10px"><ul><li>Try new things.</li><li>Respect pain points.</li><li>Learn from mistakes.</li><li>Choose courage over comfort.</li></ul></div>
    <div class="col" style="left:302px;width:165px;padding-left:10px"><ul><li>Stay true to purpose.</li><li>Maintain full view of the systems.</li><li>Steward resources wisely.</li></ul></div>
  </div>
  <div class="band gold" style="top:184px">
    <div class="col" style="left:18px;width:142px"><ul><li>Make a positive impact.</li><li>Be generous with my talent and skills.</li></ul></div>
    <div class="col" style="left:157px;width:310px;padding-left:20px"><ul><li>Disrupt oppression.</li><li>Acknowledge and challenge bias.</li><li>Center perspective of those most impacted.</li></ul></div>
  </div>
  <div class="band navy" style="top:250px">
    <div class="col" style="left:18px;width:142px"><ul><li>Practice mindfulness.</li><li>Model self-love.</li><li>Commit to authenticity.</li></ul></div>
    <div class="col" style="left:157px;width:310px;padding-left:20px"><ul><li>Express genuine appreciation.</li><li>Seek the silver linings.</li><li>Nurture optimism.</li></ul></div>
  </div>

  <div class="mini-pill cyan-pill" style="left:121px;top:47px">Trust</div>
  <div class="mini-pill cyan-pill" style="left:238px;top:47px">Kindness</div>
  <div class="mini-pill cyan-pill" style="left:418px;top:47px">Inclusion</div>
  <div class="mini-pill green-pill" style="left:121px;top:112px">Humility</div>
  <div class="mini-pill green-pill" style="left:238px;top:113px">Vulnerability</div>
  <div class="mini-pill green-pill" style="left:418px;top:112px">Excellence</div>
  <div class="mini-pill gold-pill" style="left:121px;top:178px">Service</div>
  <div class="mini-pill gold-pill" style="left:278px;top:178px">Equity</div>
  <div class="mini-pill navy-pill" style="left:121px;top:243px">Health</div>
  <div class="mini-pill navy-pill" style="left:278px;top:245px">Gratitude</div>
  <span class="page-no">1</span>
</section>

<!-- Connection -->
<section class="slide s-connection">
  <div class="photo photo-connection" role="img" aria-label="Photo of colleagues working together at a computer, darkened"></div>
  <div class="badge cyan" style="left:53px;top:50px"><span class="disc" style="color:var(--cyan)"><span class="ring"></span></span>Connection</div>
  <h2 class="headline" style="left:53px;top:116px"><b>Value-Driven</b><b>Leadership:</b><span>Connection</span></h2>
  <div class="pill cyan-pill" style="left:252px;top:20px;width:110px">TRUST</div>
  <p class="item" style="left:320px;top:61px">Be reliable</p>
  <p class="item" style="left:320px;top:85px">Right wrongs</p>
  <p class="item" style="left:320px;top:110px">Be honest</p>
  <div class="pill cyan-pill" style="left:252px;top:131px;width:110px">KINDNESS</div>
  <p class="item" style="left:321px;top:176px">Treat people as “human beings,” not “human doings.”</p>
  <p class="item" style="left:321px;top:200px">Believe that people are doing their best.</p>
  <div class="pill cyan-pill" style="left:252px;top:224px;width:110px">INCLUSION</div>
  <p class="item" style="left:322px;top:269px">Amplify voices of marginalized people.</p>
  <p class="item" style="left:322px;top:294px">Co-create safe spaces for diverse groups.</p>
</section>

<!-- Growth -->
<section class="slide s-growth">
  <div class="photo photo-growth" role="img" aria-label="Photo of a potted plant beside a letter board, darkened"></div>
  <div class="badge green" style="left:58px;top:65px"><span class="disc"><i style="left:8px;height:5px;background:var(--green)"></i><i style="left:12px;height:8px;background:var(--green)"></i><i style="left:16px;height:11px;background:var(--green)"></i></span>Growth</div>
  <h2 class="headline" style="left:62px;top:123px"><b>Value-Driven</b><b>Leadership:</b><span>Growth</span></h2>
  <div class="pill green-pill" style="left:257px;top:9px;width:110px">HUMILITY</div>
  <p class="item" style="left:326px;top:48px">Listen to learn</p>
  <p class="item" style="left:326px;top:69px">Maintain a growth mindset</p>
  <p class="item" style="left:326px;top:90px">Stay curious</p>
  <p class="item" style="left:326px;top:110px">Ask excellent questions</p>
  <div class="pill green-pill" style="left:261px;top:128px;width:110px">VULNERABILITY</div>
  <p class="item" style="left:327px;top:169px">Try new things</p>
  <p class="item" style="left:327px;top:189px">Respect pain points</p>
  <p class="item" style="left:327px;top:210px">Learn from mistakes</p>
  <p class="item" style="left:327px;top:230px">Choose courage over comfort</p>
  <div class="pill green-pill" style="left:265px;top:247px;width:110px">EXCELLENCE</div>
  <p class="item" style="left:327px;top:282px">Stay true to purpose.</p>
  <p class="item" style="left:327px;top:301px">Maintain full view of the systems.</p>
  <p class="item" style="left:327px;top:323px">Steward resources wisely.</p>
</section>

<!-- Justice -->
<section class="slide s-justice">
  <div class="photo photo-justice" role="img" aria-label="Photo of a chair holding a light box sign, darkened"></div>
  <div class="badge gold" style="left:58px;top:58px"><span class="disc" style="color:var(--gold)"><span class="ring"></span></span>Justice</div>
  <h2 class="headline" style="left:62px;top:120px"><b>Value-Driven</b><b>Leadership:</b><span>Justice</span></h2>
  <div class="pill gold-pill" style="left:264px;top:49px;width:162px">SERVICE</div>
  <p class="item" style="left:323px;top:100px">Make a positive impact.</p>
  <p class="item" style="left:323px;top:125px">Be generous with my talent and skills.</p>
  <div class="pill gold-pill" style="left:268px;top:176px;width:162px">EQUITY</div>
  <p class="item" style="left:323px;top:228px">Disrupt oppression.</p>
  <p class="item" style="left:323px;top:252px">Acknowledge and challenge bias.</p>
  <p class="item" style="left:323px;top:277px">Center perspective of those most impacted.</p>
</section>

<!-- Joy -->
<section class="slide s-joy">
  <div class="photo photo-joy" role="img" aria-label="Photo of a lakeshore at sunset, darkened"></div>
  <div class="badge navy-pill" style="left:57px;top:58px"><span class="disc" style="color:var(--navy)"><span class="ring"></span></span>Joy</div>
  <h2 class="headline" style="left:62px;top:118px"><b>Value-Driven</b><b>Leadership:</b><span>Joy</span></h2>
  <div class="pill navy-pill" style="left:267px;top:48px;width:162px">HEALTH</div>
  <p class="item" style="left:324px;top:99px">Practice mindfulness</p>
  <p class="item" style="left:324px;top:124px">Model self-love</p>
  <p class="item" style="left:324px;top:148px">Commit to authenticity</p>
  <div class="pill navy-pill" style="left:267px;top:179px;width:162px">GRATITUDE</div>
  <p class="item" style="left:324px;top:231px">Express genuine appreciation</p>
  <p class="item" style="left:324px;top:256px">Seek the silver linings</p>
  <p class="item" style="left:324px;top:280px">Nurture optimism</p>
</section>

</body>
</html>
```